Poster Design Project - Maple Bar and Restaurant

We require a Horse Racing Carnival poster (Northgate Autumn Turf Festival) to showcase the offer at our Bar/Restaurant.

The venue is called MAPLE. Our website is www.maplelounge.example.au

The venue is heavily design focused with significant use of strong graphics and logos.

The poster will need to be printed out in AO size.
Updates

Once again, thank you all for participating in this design creation. We are going to list a number of other poster briefs shortly that will require strong quirky/design graphics. I hope you'll all participate.

I am happy to provide individual responses to queries about specific designs and why they have been unsuccessful.

Overall we were really impressed with the quality of the submissions.

Thanks Gareth

Target Market(s)

Our demographic is 25-35 years old

Industry/Entity Type

Restaurant

Requirements
Must have
• The following copy needs to be incorporated into the poster -

MAPLE

AUTUMN TURF FESTIVAL 2011

Harrow Day - 29th October 2011
Champagne breakfast from 9am
Buses to and from the track
$15 bus ticket includes redeemable drink voucher
DJ from 8pm until 3am

Kestrel Plate Eve - 31st October 2011
Drink specials all night
DJ from 8pm until close

Kestrel Plate Day - 1st November 2011
Big screen racing live on 3 screens
Cocktail and drinks specials all day
DJ from 4pm

Willows Day - 3rd November 2011
DJ from 8pm until close

Lantern Day - 5th November 2011
The finishing post - Complimentary glass of sparkling with presentation of race entry ticket
DJ's from 9pm until 3am

For further enquiries and to secure your bus tickets please contact Orla on 95184726.

118 Pemberton Street, West Fairhaven Vic 3917
Tel: 95184726
Twitter: @themaplelounge
Facebook: Maple Bar and Restaurant
www.maplelounge.example.au
Should not have
• No cheesy graphics

```html
<!DOCTYPE html>
<html lang="en">
<head>
<meta charset="utf-8">
<title>Maple Bar and Restaurant – Autumn Turf Festival 2011</title>
<link href="https://fonts.googleapis.com/css2?family=Didact+Gothic&family=Arimo:wght@400&display=swap" rel="stylesheet">
<style>
  :root {
    --panel: rgba(228, 230, 168, 0.88);
    --panel-soft: rgba(236, 238, 186, 0.9);
    --olive: #75741c;
    --olive-dark: #5b5a14;
    --ink: #2f2e10;
    --white: #ffffff;
    --track: #b58c5e;
  }
  * { box-sizing: border-box; margin: 0; padding: 0; }
  html, body { width: 927px; height: 1200px; overflow: hidden; }
  body { font-family: "Arimo", Arial, sans-serif; color: var(--ink); }
  .poster { position: relative; width: 927px; height: 1200px; overflow: hidden; }

  .race-photo {
    position: absolute; inset: 0;
    background:
      radial-gradient(ellipse 260px 160px at 540px 420px, rgba(120, 40, 20, 0.85), transparent 70%),
      radial-gradient(ellipse 420px 300px at 420px 620px, rgba(110, 45, 20, 0.9), transparent 75%),
      radial-gradient(ellipse 200px 80px at 260px 230px, rgba(210, 70, 130, 0.55), transparent 70%),
      linear-gradient(180deg, #3f6b52 0%, #6c8e55 14%, #8a6a3e 34%, #7a3c1f 52%, #8c5a34 68%, var(--track) 84%, #c7a27a 100%);
  }

  .brand { position: absolute; left: 22px; top: 34px; width: 540px; text-align: center; color: var(--white); font-family: "Didact Gothic", sans-serif; }
  .brand-name { font-size: 88px; letter-spacing: 22px; line-height: 1; padding-left: 22px; }
  .brand-sub { font-size: 30px; margin-top: 22px; padding-left: 170px; text-align: left; }

  .festival-tag, .schedule, .enquiry-shape { position: absolute; }
  .festival-tag { left: 0; top: 264px; width: 380px; height: 350px; }
  .festival-text { position: absolute; left: 0; top: 264px; width: 374px; font-family: "Didact Gothic", sans-serif; color: var(--olive); }
  .festival-season { position: absolute; left: 21px; top: 58px; font-size: 58px; line-height: 1; }
  .festival-name { position: absolute; left: 40px; top: 146px; font-size: 28px; line-height: 1; white-space: nowrap; }
  .festival-year { position: absolute; left: 78px; top: 186px; font-size: 96px; line-height: 1; }

  .schedule { left: 569px; top: 0; width: 341px; height: 876px; }
  .events { position: absolute; left: 577px; top: 0; width: 330px; list-style: none; }
  .event { position: absolute; left: 0; width: 330px; }
  .event-title { display: flex; align-items: center; font-family: "Didact Gothic", sans-serif; font-size: 16px; color: var(--olive-dark); white-space: nowrap; }
  .event-title svg { width: 22px; height: 22px; margin-right: 10px; flex: none; }
  .event-details { list-style: none; margin-top: 3px; }
  .event-details li { position: relative; padding-left: 52px; font-size: 14.5px; line-height: 17px; color: var(--ink); }
  .event-details li.star::before {
    content: ""; position: absolute; left: 30px; top: 1px; width: 15px; height: 15px; background: var(--olive);
    clip-path: polygon(50% 0, 61% 35%, 98% 35%, 68% 57%, 79% 91%, 50% 70%, 21% 91%, 32% 57%, 2% 35%, 39% 35%);
  }
  .event-details li.gap { margin-top: 12px; }
  .event-details li.gap-lg { margin-top: 28px; }

  .enquiry-shape { left: 43px; top: 752px; width: 500px; height: 222px; }
  .enquiry-text { position: absolute; left: 68px; top: 798px; width: 470px; font-family: "Didact Gothic", sans-serif; font-size: 28px; line-height: 41px; color: var(--olive); }

  .contact { position: absolute; left: 569px; top: 936px; width: 341px; height: 264px; background: var(--panel-soft); border-radius: 10px 10px 0 0; padding: 24px 0 0 23px; font-family: "Didact Gothic", sans-serif; }
  .contact-address { font-size: 20px; line-height: 28px; color: var(--olive); font-style: normal; }
  .contact-tel { margin-top: 18px; font-size: 20px; color: var(--ink); }
  .contact-tel span { color: var(--olive); }
  .social { list-style: none; margin-top: 14px; }
  .social li { display: flex; align-items: center; font-size: 20px; color: var(--olive); height: 36px; margin-bottom: 12px; }
  .social-mark { width: 36px; height: 36px; border-radius: 6px; background: var(--olive); margin-right: 8px; flex: none; }
  .contact-web { position: absolute; left: 20px; bottom: 14px; font-size: 23px; color: var(--ink); }
</style>
</head>
<body>
<main class="poster">
  <div class="race-photo" role="img" aria-label="Jockeys in bright silks racing horses down a dirt track, a blurred crowd and flowers behind"></div>

  <header class="brand">
    <div class="brand-name">MAPLE</div>
    <div class="brand-sub">Bar &amp; Restaurant</div>
  </header>

  <svg class="festival-tag" viewBox="0 0 380 350" aria-hidden="true">
    <path d="M0 0 H296 Q306 0 310 9 L374 170 Q378 176 374 182 L310 341 Q306 350 296 350 H0 Z" fill="var(--panel)"/>
  </svg>
  <div class="festival-text">
    <div class="festival-season">AUTUMN</div>
    <div class="festival-name">TURF FESTIVAL</div>
    <div class="festival-year">2011</div>
  </div>

  <svg class="schedule" viewBox="0 0 341 876" aria-hidden="true">
    <path d="M0 0 H341 V743 L170 874 L0 743 Z" fill="var(--panel)"/>
  </svg>

  <ul class="events">
    <li class="event" style="top:42px">
      <div class="event-title"><svg viewBox="0 0 22 22"><path d="M0 0 H12 L22 11 L12 22 H0 Z" fill="var(--olive)"/></svg>Harrow Day - 29th October 2011</div>
      <ul class="event-details">
        <li class="star">Champagne breakfast from 9am</li>
        <li>Buses to and from the track</li>
        <li>$15 bus ticket includes redeemable drink voucher</li>
        <li class="star">DJ from 8pm until 3am</li>
      </ul>
    </li>
    <li class="event" style="top:207px">
      <div class="event-title"><svg viewBox="0 0 22 22"><path d="M0 0 H12 L22 11 L12 22 H0 Z" fill="var(--olive)"/></svg>Kestrel Plate Eve - 31st October 2011</div>
      <ul class="event-details">
        <li class="star">Drink specials all night</li>
        <li class="star gap-lg">DJ from 8pm until close</li>
      </ul>
    </li>
    <li class="event" style="top:314px">
      <div class="event-title"><svg viewBox="0 0 22 22"><path d="M0 0 H12 L22 11 L12 22 H0 Z" fill="var(--olive)"/></svg>Kestrel Plate Day - 1st November 2011</div>
      <ul class="event-details">
        <li class="star">Champagne breakfast from 9am</li>
        <li>Big screen racing live on 3 screens</li>
        <li>Cocktail and drinks specials all day</li>
        <li class="star">DJ from 4pm</li>
      </ul>
    </li>
    <li class="event" style="top:456px">
      <div class="event-title"><svg viewBox="0 0 22 22"><path d="M0 0 H12 L22 11 L12 22 H0 Z" fill="var(--olive)"/></svg>Willows Day - 3rd November 2011</div>
      <ul class="event-details">
        <li class="star">Champagne breakfast from 9am</li>
        <li>Buses to and from the track</li>
        <li>$15 bus ticket includes redeemable drink voucher</li>
        <li class="star">DJ from 8pm until close</li>
      </ul>
    </li>
    <li class="event" style="top:627px">
      <div class="event-title"><svg viewBox="0 0 22 22"><path d="M0 0 H12 L22 11 L12 22 H0 Z" fill="var(--olive)"/></svg>Lantern Day - 5th November 2011</div>
      <ul class="event-details">
        <li class="star">The finishing post - Complimentary glass of sparkling with presentation of race entry ticket</li>
        <li class="star">DJ's from 9pm until 3am</li>
      </ul>
    </li>
  </ul>

  <svg class="enquiry-shape" viewBox="0 0 500 222" aria-hidden="true">
    <path d="M22 8 Q250 -6 478 8 Q496 10 494 30 Q502 111 494 192 Q492 212 472 214 Q250 230 28 214 Q8 212 6 192 Q-2 111 6 30 Q8 10 22 8 Z" fill="var(--panel-soft)"/>
  </svg>
  <p class="enquiry-text">For further enquiries and to secure your bus tickets please contact Orla on 95184726.</p>

  <footer class="contact">
    <address class="contact-address">118 Pemberton Street,<br>West Fairhaven Vic 3917</address>
    <p class="contact-tel">Tel: <span>95184726</span></p>
    <ul class="social">
      <li><span class="social-mark"></span>@themaplelounge</li>
      <li><span class="social-mark"></span>Maple Bar and Restaurant</li>
    </ul>
    <p class="contact-web">www.maplelounge.example.au</p>
  </footer>
</main>
</body>
</html>
```